Human Resource Consulting practice needs a business card design

We need a business card design (double sided colour) for our Human Resource (HR) consulting practice in regional New South Wales, australia. Our business name is Staffwise Partners. We support small and medium business across the Mid North Coast of New South Wales by providing them with outsourced HR support, services and products to help them achieve compliance with workplace legislation and across all areas of the employment lifecycle from recruitment to termination and everything in between. Our corporate colours are hot pink and black. The final design should communicate professionalism, trust, people focus.
I have attached the current (old) business card for your reference.

Target Market(s)

Business owners and high level managers

Industry/Entity Type

Business

Contact Information for Business Card

Name
Title
Phone no
Mobile no
Address
PO Box
email address
website

Colors
e34197

Requirements
Must have
• Tempate for changing business card personal details including Name, position title, mobile number, email address.
• Keep current logo and colours as per attached
• Logo must be presented in 2 colours or black only not white
Nice to have
• One side logo and graphic only other side logo and personal details
Should not have
• Should not be the same as the current version (attached) but a modern interpretation.
• Does not need a busy reverse side with our list of services as per current version. I feel this is too busy.
• No photos

```html
<!DOCTYPE html>
<html lang="en">
<head>
<meta charset="utf-8">
<title>Staffwise Partners – Business Card</title>
<link rel="stylesheet" href="https://fonts.googleapis.com/css2?family=Michroma&display=swap">
<style>
  :root {
    --pink: #c8017d;
    --pink-soft: #e34197;
    --pink-muted: #e06aae;
    --ink: #1a1a1a;
    --paper: #f1f1f0;
    --backdrop: #2a2a2a;
  }
  * { box-sizing: border-box; margin: 0; padding: 0; }
  html, body {
    width: 1200px; height: 900px; overflow: hidden;
    background: var(--backdrop);
    font-family: "Michroma", "Arial", sans-serif;
  }
  .sheet { position: relative; width: 1200px; height: 900px; }
  .card {
    position: absolute;
    width: 700px; height: 400px;
    border-radius: 22px;
    overflow: hidden;
  }
  .card--front { left: 70px; top: 40px; background: var(--paper); }
  .card--back { left: 430px; top: 470px; background: var(--pink); }

  .brand { display: flex; align-items: center; gap: 12px; }
  .brand__dot { width: 14px; height: 14px; background: var(--pink); }
  .brand__name { font-size: 28px; color: var(--ink); letter-spacing: 0.5px; line-height: 1; }

  .card--front .brand { position: absolute; left: 48px; top: 52px; }

  .contact { position: absolute; left: 48px; top: 178px; list-style: none; color: var(--ink); font-size: 13px; line-height: 1.55; }
  .contact__address { margin-bottom: 8px; }
  .contact__item { display: flex; align-items: center; gap: 10px; }
  .contact__icon { width: 15px; height: 15px; flex: none; }

  .person { position: absolute; right: 52px; top: 196px; text-align: left; }
  .person__name { color: var(--pink); font-size: 22px; line-height: 1.1; }
  .person__title { color: var(--ink); font-size: 11px; letter-spacing: 0.5px; margin-top: 6px; }

  .band { position: absolute; left: 0; bottom: 0; width: 700px; height: 60px; }

  .card--back .brand { position: absolute; left: 50%; top: 150px; transform: translateX(-50%); white-space: nowrap; }
  .card--back .brand__dot { background: var(--ink); }
  .card--back .brand__name { font-size: 34px; }
  .card--back .web { position: absolute; left: 0; right: 0; top: 220px; text-align: center; color: var(--pink-muted); font-size: 14px; letter-spacing: 0.5px; }
</style>
</head>
<body>
<main class="sheet">
  <section class="card card--front" aria-label="Card front">
    <div class="brand">
      <span class="brand__dot"></span>
      <span class="brand__name">Staffwise Partners</span>
    </div>

    <ul class="contact">
      <li class="contact__address">PO Box 318, Kelso Bay<br>NSW 2450</li>
      <li class="contact__item">
        <svg class="contact__icon" viewBox="0 0 16 16" aria-hidden="true"><path d="M4 1.5l2.5 3-1.5 1.6c.8 1.8 2.2 3.2 4 4l1.6-1.5 3 2.5-1.6 2.4C6.7 13.6 2.4 9.3 1.6 3.1z" fill="var(--pink)"/></svg>
        <span>0400 555 218</span>
      </li>
      <li class="contact__item">
        <svg class="contact__icon" viewBox="0 0 16 16" aria-hidden="true"><rect x="1" y="3" width="14" height="10" fill="var(--pink)"/><path d="M1 3l7 6 7-6" fill="none" stroke="var(--paper)" stroke-width="1.2"/></svg>
        <span>megan@staffwisepartners.com.au</span>
      </li>
      <li class="contact__item">
        <svg class="contact__icon" viewBox="0 0 16 16" aria-hidden="true"><g fill="none" stroke="var(--pink)" stroke-width="1.2"><circle cx="8" cy="8" r="6.5"/><ellipse cx="8" cy="8" rx="3" ry="6.5"/><path d="M1.5 8h13M2.5 4.8h11M2.5 11.2h11"/></g></svg>
        <span>www.staffwisepartners.com.au</span>
      </li>
    </ul>

    <div class="person">
      <p class="person__name">Megan Hale</p>
      <p class="person__title">PRINCIPAL CONSULTANT</p>
    </div>

    <svg class="band" viewBox="0 0 700 60" aria-hidden="true">
      <polygon points="0,40 330,40 360,0 420,0 450,40 700,40 700,60 0,60" fill="var(--pink)"/>
    </svg>
  </section>

  <section class="card card--back" aria-label="Card back">
    <div class="brand">
      <span class="brand__dot"></span>
      <span class="brand__name">Staffwise Partners</span>
    </div>
    <p class="web">www.staffwisepartners.com.au</p>
  </section>
</main>
</body>
</html>
```